Window Advertisment for Rentals Company

I own a property rental company in Cyprus and I am looking for an eye catching design to place in my window to attract passers by.

Please check the attachment for more details.

Ad size to be 309cm x 204cm landscape

The font of the logo is velocity

Target Market(s)

Property Owners

Industry/Entity Type

It Company

Requirements
Must have
• The colours from my logo and be eye catching and make passers by take notice

```html
<!DOCTYPE html>
<html lang="en">
<head>
<meta charset="utf-8">
<title>Harbour Stays Cyprus – Window Advert</title>
<link rel="stylesheet" href="https://fonts.googleapis.com/css2?family=Baumans&family=PT+Sans&family=Russo+One&family=Roboto+Condensed:wght@700&display=swap">
<style>
  :root {
    --orange: #f27428;
    --yellow: #f9c414;
    --yellow-deep: #f0a81a;
    --cream: #fdf0dc;
    --white: #ffffff;
    --sea: #3fa7c0;
    --sea-light: #7cc7d3;
    --sand: #e6cf9c;
  }
  html, body {
    margin: 0;
    padding: 0;
    width: 1200px;
    height: 852px;
    overflow: hidden;
    background: var(--orange);
  }
  .advert {
    position: relative;
    width: 1200px;
    height: 852px;
    background: var(--orange);
    overflow: hidden;
  }
  .headline {
    position: absolute;
    left: 62px;
    top: 70px;
    margin: 0;
    font-family: "Baumans", sans-serif;
    font-weight: 400;
    font-size: 61px;
    line-height: 76px;
    color: var(--yellow);
    letter-spacing: 0.5px;
  }
  .beach-strip {
    position: absolute;
    left: 0;
    top: 305px;
    width: 670px;
    height: 245px;
  }
  .benefits {
    position: absolute;
    left: 72px;
    top: 592px;
    margin: 0;
    width: 460px;
    font-family: "PT Sans", sans-serif;
    font-size: 22.5px;
    line-height: 47px;
    color: var(--cream);
    text-transform: uppercase;
  }
  .benefits .dot { font-size: 16px; vertical-align: 2px; padding: 0 3px 0 0; }
  .brand {
    position: absolute;
    left: 680px;
    top: 500px;
    display: flex;
    align-items: center;
    gap: 16px;
  }
  .brand-mark {
    width: 58px;
    height: 58px;
    border-radius: 50%;
    background: var(--yellow);
    flex: none;
  }
  .brand-name {
    font-family: "Baumans", sans-serif;
    font-size: 60px;
    line-height: 58px;
    color: var(--yellow);
  }
  .contact {
    position: absolute;
    right: 50px;
    text-align: right;
    margin: 0;
  }
  .contact-tel {
    top: 650px;
    font-family: "Russo One", sans-serif;
    font-size: 56px;
    line-height: 64px;
    color: var(--yellow);
    letter-spacing: 1px;
  }
  .contact-web {
    top: 735px;
    font-family: "Roboto Condensed", sans-serif;
    font-weight: 700;
    font-size: 30px;
    line-height: 36px;
    color: var(--white);
    letter-spacing: 3.6px;
  }
</style>
</head>
<body>
<main class="advert">
  <h1 class="headline">We are looking for villas and apartments,<br>to fulfill our growing demand of rentals</h1>

  <svg class="beach-strip" viewBox="0 0 670 245" role="img" aria-label="Photo of a sandy beach with rows of yellow parasols in front of a turquoise sea, peeling back like paper">
    <defs>
      <linearGradient id="beachTones" x1="0" y1="0" x2="0" y2="1">
        <stop offset="0" stop-color="var(--sea)"/>
        <stop offset="0.38" stop-color="var(--sea-light)"/>
        <stop offset="0.45" stop-color="#e9b932"/>
        <stop offset="0.7" stop-color="var(--sand)"/>
        <stop offset="1" stop-color="#d9bf8c"/>
      </linearGradient>
      <linearGradient id="curlTones" x1="0" y1="0" x2="1" y2="0">
        <stop offset="0" stop-color="var(--yellow-deep)"/>
        <stop offset="0.55" stop-color="var(--yellow)"/>
        <stop offset="1" stop-color="var(--yellow-deep)"/>
      </linearGradient>
    </defs>
    <path d="M0 20 L590 14 L590 232 L0 240 Z" fill="url(#beachTones)"/>
    <path d="M586 6 Q600 0 660 6 L650 230 Q640 245 620 242 L580 240 Z" fill="url(#curlTones)"/>
  </svg>

  <p class="benefits">
    <span class="dot">•</span>Low commissions &nbsp;<span class="dot">•</span>Quick payouts<br>
    <span class="dot">•</span>Free advertising &nbsp;<span class="dot">•</span>Connect with<br>
    over 35 leading websites &nbsp;<span class="dot">•</span>Be seen by<br>
    100+ million travellers per month
  </p>

  <div class="brand">
    <span class="brand-mark"></span>
    <span class="brand-name">harbour<br>stays cyprus</span>
  </div>

  <p class="contact contact-tel">TEL: 23 555014</p>
  <p class="contact contact-web">WWW.HARBOURSTAYSCYPRUS.COM</p>
</main>
</body>
</html>
```